Webdesign für SEO-Agentur
Zielgruppe
Wir bieten kleinen und mittelständischen Unternehmen Suchmaschinenoptimierung zum fairen Preis mit Erfolgsgarantie an. Unsere Zielgruppe sind Unternehmer die bisher wenig oder gar keine Erfahrungen mit SEO hatten. Wir möchten Unternehmen dabei helfen ihren digitalen Auftritt sowie dessen Sichtbarkeit zu verbessern um neue Kunden zu finden.
Aufgabenstellung
- seriöses und modernes Design bei gleichzeitig ansprechender Gestaltung
- passend zum Namen möchten wir, dass die Website einen leichten wissenschaftlichen/chemischen Touch erhält. Beachten Sie daher unsere Skizze zur Schritt für Schritt Darstellung. Weitere kleine Hinweise in Richtung Chemie oder Wissenschaft können und sollen eingebaut werden.
- vorerst nur Landing-Page, daher keine Navigation nötig. Wir erwarten eine vollständige Desktop sowie Mobilversion in Ihrem Design.
- Einhaltung der vorgegebenen Inhalte
- keine langweiligen Standard-Designs, auch besondere Seiten können seriös sein
- Header ist für Portrait der Mitarbeiter reserviert und benötigt daher eine gewisse freie Fläche

```html
<!DOCTYPE html>
<html lang="de">
<head>
<meta charset="utf-8">
<title>Valenzwerk – SEO-Agentur</title>
<link href="https://fonts.googleapis.com/css2?family=Lato:wght@300;400;700&display=swap" rel="stylesheet">
<style>
  :root {
    --navy: #173a68;
    --deep-navy: #0f3864;
    --red: #ec174b;
    --text: #5f6368;
    --muted: #9a9ca3;
    --bg: #f7f7f9;
    --card: #ffffff;
  }
  * { box-sizing: border-box; margin: 0; padding: 0; }
  html, body { width: 1200px; height: 3094px; overflow: hidden; }
  body {
    background: var(--bg);
    font-family: "Lato", Arial, sans-serif;
    color: var(--text);
    position: relative;
  }
  .page { position: relative; width: 1200px; height: 3094px; overflow: hidden; }
  .deco { position: absolute; left: 0; top: 0; }

  .brand {
    position: absolute; left: 79px; top: 62px;
    font-size: 34px; font-weight: 700; color: var(--navy);
    display: flex; align-items: center; gap: 10px;
  }
  .brand-dot { width: 12px; height: 12px; border-radius: 50%; background: var(--red); }

  .hero-title {
    position: absolute; left: 79px; top: 254px; width: 520px;
    font-size: 35px; line-height: 41px; font-weight: 700; color: var(--navy);
  }
  .hero-lead {
    position: absolute; left: 79px; top: 344px; width: 480px;
    font-size: 22px; line-height: 31px; font-weight: 300; color: var(--muted);
  }
  .btn {
    position: absolute; display: flex; align-items: center; justify-content: center;
    background: var(--red); color: #fff; border-radius: 24px;
    font-size: 17px; font-weight: 400; text-decoration: none; height: 48px;
  }
  .btn-hero { left: 79px; top: 441px; width: 234px; }

  .molecule-icon { position: absolute; left: 568px; top: 588px; }

  .success-title {
    position: absolute; left: 300px; top: 698px; width: 600px;
    text-align: center; font-size: 35px; line-height: 41px; font-weight: 700; color: var(--navy);
  }
  .success-text {
    position: absolute; left: 262px; top: 802px; width: 676px;
    text-align: center; font-size: 16.5px; line-height: 24.4px; font-weight: 300; color: var(--text);
  }
  .btn-consult { left: 392px; top: 1015px; width: 417px; }

  .info-col { position: absolute; top: 1228px; width: 506px; }
  .info-col h3 { font-size: 17px; font-weight: 700; color: var(--red); margin-bottom: 24px; }
  .info-col p { font-size: 15px; line-height: 22.6px; font-weight: 300; color: var(--text); }
  .info-left { left: 79px; }
  .info-right { left: 614px; }

  .why-title {
    position: absolute; left: 79px; top: 1606px;
    font-size: 35px; font-weight: 700; color: var(--navy);
  }
  .why-sub {
    position: absolute; left: 79px; top: 1656px;
    font-size: 22px; font-weight: 300; color: var(--muted);
  }
  .why-text {
    position: absolute; left: 79px; top: 1712px; width: 790px;
    font-size: 17px; line-height: 24.4px; font-weight: 300; color: var(--text);
  }

  .card {
    position: absolute; width: 328px; background: var(--card);
    box-shadow: 0 2px 10px rgba(20, 40, 80, 0.06);
  }
  .card-photo { width: 100%; height: 218px; }
  .card-body { padding: 34px 28px 28px; }
  .card h4 { font-size: 17px; line-height: 21px; font-weight: 700; color: var(--red); margin-bottom: 19px; }
  .card p { font-size: 14.5px; line-height: 22.6px; font-weight: 300; color: var(--text); }
  .col-1 { left: 79px; } .col-2 { left: 436px; } .col-3 { left: 791px; }
  .row-1 { top: 1952px; height: 479px; }
  .row-2 { top: 2500px; height: 487px; }
</style>
</head>
<body>
<div class="page">
  <svg class="deco" width="1200" height="3094" viewBox="0 0 1200 3094" aria-hidden="true">
    <defs>
      <linearGradient id="heroTone" x1="0" y1="0" x2="1" y2="1">
        <stop offset="0" stop-color="#e9ecef"/>
        <stop offset="0.45" stop-color="#c9a45a"/>
        <stop offset="0.75" stop-color="#4d6a92"/>
        <stop offset="1" stop-color="#2b2f38"/>
      </linearGradient>
    </defs>
    <polygon points="468,0 1200,0 1200,300 760,300" fill="#ececef"/>
    <path d="M560,0 L1200,0 L1200,340 L1146,402 Q1060,500 968,518 Q930,524 905,492 L735,276 Z" fill="url(#heroTone)" role="img" aria-label="Foto: drei Mitarbeitende im Büro schauen gemeinsam auf ein Tablet"/>
    <path d="M0,684 L150,790 Q205,830 180,900 L0,1224 Z" fill="var(--red)"/>
    <path d="M1200,1368 L970,1560 Q920,1610 960,1690 L1200,2028 Z" fill="var(--deep-navy)"/>
  </svg>

  <div class="brand"><span class="brand-dot"></span>Valenzwerk</div>

  <h1 class="hero-title">Bereit für das nächste Element der Suchmaschinenoptimierung?</h1>
  <p class="hero-lead">Valenzwerk ist Ihre SEO-Agentur für mehr Sichtbarkeit, mehr Reichweite und mehr Traffic</p>
  <a class="btn btn-hero" href="#">Mit Erfolgsgarantie</a>

  <svg class="molecule-icon" width="64" height="60" viewBox="0 0 64 60" aria-hidden="true" fill="none" stroke="var(--red)" stroke-width="2.2">
    <circle cx="8" cy="8" r="5"/><circle cx="56" cy="8" r="5"/>
    <circle cx="8" cy="52" r="5"/><circle cx="56" cy="52" r="5"/>
    <circle cx="32" cy="30" r="6"/><circle cx="32" cy="55" r="4"/><circle cx="60" cy="30" r="3.5"/>
    <line x1="12" y1="12" x2="27" y2="26"/><line x1="52" y1="12" x2="37" y2="26"/>
    <line x1="12" y1="48" x2="27" y2="34"/><line x1="52" y1="48" x2="37" y2="34"/>
    <line x1="32" y1="36" x2="32" y2="51"/><line x1="38" y1="30" x2="56.5" y2="30"/>
  </svg>

  <h2 class="success-title">Abrechnung auf Erfolgsbasis – garantiert!</h2>
  <p class="success-text">Wie jetzt? Erst bezahlen, wenn die Optimierung erfolgreich war? Genauso ist es! Als erfahrene SEO Agentur bietet wir unsere Leistungen als eine der wenigen zu 100 Prozent auf Erfolgsbasis an. Das heißt, dass Sie von uns erst dann eine Rechnung erhalten, wenn Ihre Webseite auf der 1. Seite der Suchergebnisse rankt. Durch die präzise Zielvorgabe ist sichergestellt, dass Sie keinerlei Risiko eingehen und wir wie immer unser Bestes geben. Warum wir das machen? Weil wir über Jahre hinweg die perfekte Strategie für ein besseres Ranking erforscht haben und damit bisher noch jeden Kunden nach vorne gebracht haben.</p>
  <a class="btn btn-consult" href="#">Jetzt unverbindliche Beratung vereinbaren</a>

  <section class="info-col info-left">
    <h3>Was ist SEO?</h3>
    <p>SEO steht für Search Engine Optimization, zu Deutsch Suchmaschinenoptimierung, und ist eine der wichtigsten Disziplinen im Online Marketing. Wer heute Informationen benötigt oder ein Problem lösen will, der konsultiert eine Suchmaschine – allen voran Findora. Doch eins wissen Sie selbst am besten: Kaum jemand schaut sich die Suchergebnisse außerhalb von Seite eins ein. Umso wichtiger ist es, mit seiner Webseite genau hier zu ranken. Das aber wollen viele, deshalb führt für erfolgreiche Webseiten kein Weg an der Suchmaschinenoptimierung vorbei. Wir als SEO Agentur unterstützen Sie dabei, aus den zahlreichen Elementen, die für die Suchmaschinenoptimierung notwendig sind, eine funktionierende Verbindung zu schaffen.</p>
  </section>
  <section class="info-col info-right">
    <h3>Was bringt SEO?</h3>
    <p>Eine prominente Position in den Suchergebnissen führt zu einer Kettenreaktion, die sich jeder Unternehmer wünscht. Je besser Sichtbarkeit und Reichweite, desto mehr Traffic spült Findora auf Ihre Webseite. Wir als führende SEO Agentur sorgen dafür, dass es sich dabei um qualifizierten Traffic handelt, aus dem auch zahlende Kunden werden. Dadurch steigt nicht nur Ihre Konversionsrate, sondern natürlich auch der Umsatz Ihres Unternehmens. Suchmaschinenoptimierung macht sich also bezahlt!</p>
  </section>

  <h2 class="why-title">Warum wir?</h2>
  <p class="why-sub">SEO Agentur mit Herz, Verstand und ganz viel Erfahrung</p>
  <p class="why-text">Seit über zehn Jahren forschen wir schwerpunktmäßig an der perfekten Zusammensetzung effektiver Suchmaschinenoptimierung. Als reine SEO Agentur haben wir uns ganz bewusst dafür entschieden, nicht die gesamte Palette des Online Marketings anzubieten, sondern das, wofür unser Herz schlägt und das, was den größten und vor allem nachhaltigsten Erfolg verspricht. Seitdem ist SEO mehr als unser Forschungsgebiet. SEO ist unsere Leidenschaft. Und genau die Liebe zu dem, was wir tun, macht uns so gut, dass wir ausschließlich auf Erfolgsbasis arbeiten.</p>

  <article class="card col-1 row-1">
    <div class="card-photo" role="img" aria-label="Foto: Anwalt mit Akte im Büro" style="background:linear-gradient(135deg,#e4e2dc,#3a3f4a 60%,#d9d6cf)"></div>
    <div class="card-body"><h4>SEO für Anwälte und Steuerberater</h4>
      <p>Große Rechtanwalts- und Steuerberaterkanzleien dominieren den Markt. Mit SEO können sich auch kleine und regionale Anwälte, Notare, Steuer- und Unternehmensberater durchsetzen. Wir helfen Ihnen, sich online als Experte zu profilieren.</p></div>
  </article>
  <article class="card col-2 row-1">
    <div class="card-photo" role="img" aria-label="Foto: Arzt berät eine Patientin" style="background:linear-gradient(135deg,#f1f1f1,#d8d3cc 50%,#a27b5c)"></div>
    <div class="card-body"><h4>SEO für Ärzte und Apotheker</h4>
      <p>Ärzte und Apotheker können mit einer suchmaschinen-optimierten Webseite nicht nur neue Patienten und Kunden gewinnen, sondern diesen auch langfristig binden und ihnen zeitgemäße Serviceleistungen anbieten.</p></div>
  </article>
  <article class="card col-3 row-1">
    <div class="card-photo" role="img" aria-label="Foto: Übergabe eines Versandpakets" style="background:linear-gradient(135deg,#d9c39a,#c9a46e 50%,#6f8fa8)"></div>
    <div class="card-body"><h4>SEO für (Online-)Händler</h4>
      <p>Der Online-Handel boomt, entsprechend groß ist auch die Konkurrenz. Ein Online-Shop ist noch lange kein Selbstläufer und bedarf besonderen Know-hows bei der Suchmaschinen-optimierung. Wir steigern Ihre Verkaufszahlen nachhaltig!</p></div>
  </article>

  <article class="card col-1 row-2">
    <div class="card-photo" role="img" aria-label="Foto: Handwerker mit Werkzeuggürtel in der Werkstatt" style="background:linear-gradient(135deg,#8a6f54,#3d4a63 55%,#b08a5c)"></div>
    <div class="card-body"><h4>SEO für Handwerker und Dienstleister</h4>
      <p>Wer einen Handwerker oder Dienstleister sucht, der schaut nicht mehr in die Blauen Blätter, sondern sucht online. Ohne sichtbare Webseite sind Sie für den Kunden quasi nicht existent. Mit Local SEO lässt sich das bereits mit einfachen Mitteln und für kleines Geld ändern!</p></div>
  </article>
  <article class="card col-2 row-2">
    <div class="card-photo" role="img" aria-label="Foto: Skizzen von Webseiten-Layouts an einer Glaswand" style="background:linear-gradient(135deg,#eef0f2,#c9ced4 55%,#3a3d44)"></div>
    <div class="card-body"><h4>SEO für Online-Portale</h4>
      <p>Online-Portale sind von den Suchmaschinen so abhängig wie kaum ein anderes Internetangebot. Nur wer bei Findora ganz oben steht, erhält ausreichend Traffic um zu überleben. Wir sichern die Zukunft Ihres Portals und bringen Sie in die schwarzen Zahlen.</p></div>
  </article>
  <article class="card col-3 row-2">
    <div class="card-photo" role="img" aria-label="Foto: Team arbeitet gemeinsam am Computer" style="background:linear-gradient(135deg,#e6e8ea,#5b7394 50%,#2a2c33)"></div>
    <div class="card-body"><h4>SEO für Sie</h4>
      <p>Es gibt keine Branche, die heutzutage ohne Suchmaschinenoptimierung auskommt. Mit zielgerichteten Maßnahmen setzen wir auch Ihr Business auf ein neues Level, ganz egal wie groß Ihr Unternehmen ist. Sprechen Sie uns noch heute an!</p></div>
  </article>
</div>
</body>
</html>
```